Website design for an Italian restaurant in Amsterdam

I need a design for a client of mine. It is for Teatro Lucerna, an Italian restaurant in Amsterdam.
We are going for a clean, modern look but we also need to realise an authentic feel.
The restaurant is located in an old movie theatre, that is where the name Teatro Lucerna comes from.
Industry/Entity Type
Italian Restaurant
Number of Pages Required
1 page
Font styles to use
Sans Serif
Colors
Designer to choose colors to be used in the design.

```html
<!DOCTYPE html>
<html lang="en">
<head>
<meta charset="utf-8">
<title>Teatro Lucerna – Ristorante Italiano</title>
<link rel="stylesheet" href="https://fonts.googleapis.com/css2?family=Bodoni+Moda:wght@400;500&family=Jost:wght@400;500;600&display=swap">
<style>
:root{
  --rose:#b14f5e;
  --rose-soft:#c98a93;
  --ink:#1f1f1f;
  --text:#555;
  --muted:#888;
  --line:#d9d9d9;
  --paper:#ffffff;
  --serif:"Bodoni Moda", "Didot", serif;
  --sans:"Jost", "Futura", sans-serif;
}
*{box-sizing:border-box;margin:0;padding:0}
html,body{width:1200px;height:3644px;overflow:hidden;background:var(--paper)}
body{position:relative;font-family:var(--sans);color:var(--ink)}
.abs{position:absolute}
.btn-outline{position:absolute;border:2px solid var(--rose);color:var(--rose);font:500 13px/1 var(--sans);letter-spacing:2px;text-transform:uppercase;display:flex;align-items:center;justify-content:center;background:#fff}
.btn-solid{position:absolute;background:var(--rose);color:#fff;font:500 13px/1 var(--sans);letter-spacing:2px;text-transform:uppercase;display:flex;align-items:center;justify-content:center}
.btn-white{position:absolute;background:#fff;color:var(--rose);font:500 13px/1 var(--sans);letter-spacing:2px;text-transform:uppercase;display:flex;align-items:center;justify-content:center}

/* header */
.brand{position:absolute;left:0;width:1200px;top:18px;text-align:center}
.brand-dot{width:34px;height:34px;border-radius:50%;border:2px solid var(--rose);margin:0 auto 6px}
.brand-name{font:500 27px/1 var(--serif);letter-spacing:1px;color:var(--ink);text-transform:uppercase}
.brand-tag{font:400 16px/1.3 var(--sans);color:var(--rose);margin-top:2px}
.nav a{position:absolute;top:88px;font:600 12.5px/1 var(--sans);letter-spacing:2px;color:var(--ink);text-decoration:none;text-transform:uppercase}
.nav a.active{color:var(--rose)}
.nav a.active::after{content:"";position:absolute;left:0;right:0;bottom:-8px;height:2px;background:var(--rose)}

/* hero */
.hero{left:61px;top:140px;width:1088px;height:558px;background:linear-gradient(180deg,#3a3a38 0%,#5a5750 45%,#6e6a62 70%,#3b3a36 100%)}
.hero-sub{left:61px;width:1088px;top:333px;text-align:center;color:#fff;font:500 22px/1 var(--sans);letter-spacing:1px}
.hero-title{left:61px;width:1088px;top:368px;text-align:center;color:#fff;font:400 58px/1 var(--serif);letter-spacing:2px}

/* about */
.about-title{left:176px;top:792px;font:500 22px/1 var(--sans);letter-spacing:.5px}
.about-title span{color:var(--rose)}
.about-text{left:176px;top:850px;width:470px;font:400 14px/1.65 var(--sans);color:var(--text)}
.about-photo{left:708px;top:771px;width:323px;height:299px;background:linear-gradient(135deg,#6f7b70 0%,#4a4f47 45%,#8d5f45 75%,#3a3530 100%)}

/* special menu */
.menu-band{left:61px;top:1146px;width:1088px;height:372px;background:linear-gradient(180deg,#6a6a66 0%,#58574f 55%,#454540 100%)}
.menu-title{left:61px;width:1088px;top:1270px;text-align:center;color:#fff;font:400 64px/1 var(--serif);letter-spacing:3px}
.menu-sub{left:61px;width:1088px;top:1352px;text-align:center;color:#fff;font:500 22px/1 var(--sans)}
.tabs{left:384px;top:1499px;width:441px;height:39px;display:flex;background:#fff;border:1px solid var(--line)}
.tab{flex:1;display:flex;align-items:center;justify-content:center;font:500 12.5px/1 var(--sans);letter-spacing:2px;text-transform:uppercase;color:var(--ink);border-right:1px solid var(--line)}
.tab:last-child{border-right:0}
.tab.active{background:var(--rose);color:#fff;position:relative}
.tab.active::after{content:"";position:absolute;bottom:-10px;left:50%;margin-left:-10px;border:10px solid transparent;border-bottom:0;border-top-color:var(--rose)}
.dish{top:1585px;width:262px;height:232px;display:flex;align-items:center;justify-content:center;color:#fff;font:500 20px/1 var(--sans)}

/* sunday band */
.sunday{left:61px;top:1969px;width:1088px;height:370px;background:linear-gradient(90deg,#2e2a3a 0%,#3b3553 40%,#2c2a44 70%,#1f2030 100%)}
.sunday-kicker{left:61px;width:1088px;top:2021px;text-align:center;color:#fff;font:500 22px/1 var(--sans)}
.sunday-title{left:61px;width:1088px;top:2060px;text-align:center;color:#fff;font:400 54px/1 var(--serif);letter-spacing:4px;text-transform:uppercase}
.sunday-sub{left:61px;width:1088px;top:2126px;text-align:center;color:#fff;font:500 22px/1 var(--sans)}
.sunday-hours{left:61px;width:1088px;top:2172px;text-align:center;color:#fff;font:500 14px/1 var(--sans);letter-spacing:1.5px}

/* gallery */
.gallery-title{left:0;width:1200px;top:2404px;text-align:center;font:400 56px/1 var(--serif);letter-spacing:4px;color:var(--ink)}
.ph{position:absolute}
.arrow{position:absolute;width:30px;height:30px;border-radius:50%;display:flex;align-items:center;justify-content:center}

/* map & contact */
.map{left:61px;top:3240px;width:735px;height:372px;background:linear-gradient(135deg,#e9e9e9 0%,#dcdcdc 50%,#e6e6e6 100%)}
.contact-rule{left:855px;top:3252px;width:30px;height:2px;background:var(--rose)}
.contact-title{left:855px;top:3268px;font:600 14px/1 var(--sans);letter-spacing:2px;color:var(--rose);text-transform:uppercase}
.contact-addr{left:855px;top:3318px;font:400 14px/1.6 var(--sans);color:var(--text)}
.contact-phone{left:855px;top:3366px;font:600 15px/1 var(--sans);color:var(--rose);letter-spacing:1px}
.contact-mail{left:855px;top:3395px;font:400 14px/1 var(--sans);color:var(--text)}
.social{position:absolute;top:3574px;width:38px;height:38px;border-radius:50%;border:1.5px solid var(--rose)}
.copyright{left:0;width:1200px;top:3627px;text-align:center;font:400 11px/1 var(--sans);letter-spacing:1.5px;color:var(--text)}
</style>
</head>
<body>

<header>
  <div class="btn-outline" style="left:88px;top:28px;width:206px;height:30px;font-size:12px;">Call: [+31] 20 555 0182</div>
  <div class="btn-outline" style="left:916px;top:28px;width:206px;height:30px;font-size:12px;">Reservation</div>
  <div class="brand">
    <div class="brand-dot"></div>
    <div class="brand-name">Teatro Lucerna</div>
    <div class="brand-tag">Ristorante Italiano</div>
  </div>
  <nav class="nav">
    <a class="active" style="left:88px">Home</a>
    <a style="left:203px">About</a>
    <a style="left:322px">Menu (New)</a>
    <a style="left:795px">Group Menu</a>
    <a style="left:944px">Gallery</a>
    <a style="left:1060px">Contact</a>
  </nav>
</header>

<section class="hero-section">
  <div class="abs hero" role="img" aria-label="Photo of the modern restaurant dining room with tables, chairs and an open bar"></div>
  <div class="abs hero-sub">Lantaarnkade 27</div>
  <div class="abs hero-title">IN THE CITY CENTER</div>
  <div class="btn-white" style="left:530px;top:458px;width:150px;height:40px;font-size:12px;">Contact us</div>
  <svg class="abs" style="left:596px;top:640px" width="16" height="10" viewBox="0 0 16 10"><path d="M2 2l6 6 6-6" fill="none" stroke="#fff" stroke-width="2"/></svg>
</section>

<section class="about">
  <h2 class="abs about-title">About the <span>Teatro Lucerna</span></h2>
  <p class="abs about-text">There are many variations of passages of Lorem Ipsum available, but the majority have suffered alteration in some form, by injected humour, or randomised words which don't look even slightly believable. If you are going to use a passage of Lorem Ipsum, you need to be sure there isn't anything embarrassing hidden in the middle of text. All the Lorem Ipsum generators ...</p>
  <div class="btn-solid" style="left:176px;top:1007px;width:148px;height:38px;font-size:12px;">Discover more</div>
  <div class="abs about-photo" role="img" aria-label="Photo of the restaurant kitchen with cooks at work"></div>
</section>

<section class="special-menu">
  <div class="abs menu-band" role="img" aria-label="Photo of chefs cooking in a professional kitchen"></div>
  <h2 class="abs menu-title">OUR SPECIAL MENU</h2>
  <div class="abs menu-sub">Flourant Tasty</div>
  <div class="abs tabs">
    <div class="tab active">Menu (New)</div>
    <div class="tab">Group Menu</div>
    <div class="tab">Wijnen</div>
  </div>
  <div class="abs dish" style="left:176px;background:linear-gradient(135deg,#3a2a22,#7a3d26 50%,#2b211c)" role="img" aria-label="Photo of grilled skewers as appetizers">Appetizers</div>
  <div class="abs dish" style="left:473px;background:linear-gradient(135deg,#2c2c2a,#5b6b4a 50%,#262624)" role="img" aria-label="Photo of a fresh tomato and herb salad">Salads</div>
  <div class="abs dish" style="left:771px;background:linear-gradient(135deg,#3a3632,#8a8276 50%,#34302b)" role="img" aria-label="Photo of pasta with clams">The Pasta</div>
  <div class="btn-outline" style="left:529px;top:1854px;width:149px;height:39px;font-size:12px;">View all menu</div>
</section>

<section class="open-sunday">
  <div class="abs sunday" role="img" aria-label="Photo of a set table in the warmly lit dining room"></div>
  <div class="abs sunday-kicker">Now Open on Sundays!</div>
  <h2 class="abs sunday-title">Teatro Lucerna</h2>
  <div class="abs sunday-sub">Italian Restaurant</div>
  <div class="abs sunday-hours">TUE - SUN: 18:00 - 23:00 &nbsp;|&nbsp; MON - CLOSED</div>
  <div class="btn-white" style="left:442px;top:2229px;width:324px;height:48px;font-size:13px;">Book your favorite table</div>
</section>

<section class="gallery">
  <h2 class="abs gallery-title">PHOTO GALLERY</h2>
  <div class="arrow" style="left:990px;top:2512px;background:#9a9a9a"><svg width="10" height="12" viewBox="0 0 10 12"><path d="M7 1L2 6l5 5" fill="none" stroke="#fff" stroke-width="2"/></svg></div>
  <div class="arrow" style="left:1031px;top:2512px;background:#1f1f1f"><svg width="10" height="12" viewBox="0 0 10 12"><path d="M3 1l5 5-5 5" fill="none" stroke="#fff" stroke-width="2"/></svg></div>
  <div class="ph" style="left:147px;top:2571px;width:264px;height:265px;background:linear-gradient(135deg,#3a3330,#7a4a3a 55%,#2c2623)" role="img" aria-label="Photo of the open kitchen counter"></div>
  <div class="ph" style="left:441px;top:2510px;width:326px;height:326px;background:linear-gradient(135deg,#5a5a56,#8c8a84 50%,#3c3b38)" role="img" aria-label="Photo of a chef plating a dish"></div>
  <div class="ph" style="left:796px;top:2571px;width:264px;height:265px;background:linear-gradient(135deg,#b86e78,#a34c5c 55%,#8c4050)" role="img" aria-label="Photo of guests dining, highlighted"></div>
  <svg class="abs" style="left:910px;top:2685px" width="36" height="36" viewBox="0 0 36 36"><path d="M18 0v36M0 18h36" stroke="#fff" stroke-width="1.5"/></svg>
  <div class="ph" style="left:291px;top:2865px;width:167px;height:167px;background:linear-gradient(135deg,#2e241e,#7b3f26 50%,#2a201b)" role="img" aria-label="Photo of grilled skewers"></div>
  <div class="ph" style="left:487px;top:2865px;width:233px;height:233px;background:linear-gradient(135deg,#4a2a2e,#6e3a3a 45%,#8a8478 70%,#3a3230)" role="img" aria-label="Photo of a plated dish with wine glasses"></div>
  <div class="ph" style="left:749px;top:2865px;width:167px;height:167px;background:linear-gradient(135deg,#3a3430,#7d7468 50%,#2e2a26)" role="img" aria-label="Photo of a table setting with candles"></div>
  <div class="btn-outline" style="left:541px;top:3127px;width:128px;height:39px;font-size:12px;">View all</div>
</section>

<footer>
  <div class="abs map" role="img" aria-label="Street map showing the restaurant location"></div>
  <div class="abs contact-rule"></div>
  <h3 class="abs contact-title">Contact us</h3>
  <div class="abs contact-addr">Teatro Lucerna<br>Lantaarnkade 27 1016 ZT Amsterdam.</div>
  <div class="abs contact-phone">CALL: +31 20 555 0182</div>
  <div class="abs contact-mail">E: info@teatrolucerna.com</div>
  <div class="btn-solid" style="left:855px;top:3437px;width:168px;height:36px;font-size:12px;">Book your table</div>
  <div class="social" style="left:857px"></div>
  <div class="social" style="left:906px"></div>
  <div class="abs copyright">© 2018 TEATRO LUCERNA</div>
</footer>

</body>
</html>
```